Integrative Medical Practice Website Redo

I am needing to have our current website redesigned to make it a responsive website to work on smartphones.
Current website
www.brightoakfm.com
Here are several examples of what I am looking for
https://www.corvanhealth.com/
I am wanting a popup for a newsletter signup
Looking for a very professional, clean, simple, minimalist, bold well designed website
Colors would ideally be greens and blues, cool tones, muted colors, or graytones like:
https://journeybright.org/
Several other clean design examples
http://7harborsrenton.com/
http://www.belvomedical.com/
http://sunpathyouth.com/
http://yourcellduke.com/
I would like the top navigation bar to be able to slide down while browsing site
We are also needing to add several features that are not on our current website:
Questionnaire buttons
Are you toxic questionnaire?
Take our hormone quiz to find out if hormones are affecting your health.
online scheduling option for:
nutrition counselling
testing like body composition, basal metabolic rate, CIMT, breast thermography, VO2 Max testing, Vita Trace
Therapies like whole body vibration, infrared sauna, Exercise with oxygen, hyperbaric oxygen, spinal decompression
Need to have separate page for different services and split up services into:
Consults/Office Visits, Testing, Therapies, Procedures
Need to have a button link to patient portal
Needs to have online store
Need to add navigation button "Start Here"
Need a spot for a video on practice summary
Newsletter signup to collect emails
Testimonials from linkpage
Blog that posts can be shared with social media
Password protected patient access that can integrate into crate.net ideally
Modules for programs online classes/videos
I have attached stock images that you can use, but feel free to find others to use.
I have also attached a copy of our current brochure that shows an overview of the practice
Target Market(s)
Health conscious people of all ages looking for a family medicine doctor
Industry/Entity Type
Alternative Medicine
Coding
Coded - Design and coding required
Number of Pages Required
5+ page
Look and feel

```html
<!DOCTYPE html>
<html lang="en">
<head>
<meta charset="utf-8">
<title>Bright Oak Family Medicine – Home</title>
<link href="https://fonts.googleapis.com/css2?family=Raleway:wght@400;500&family=Ubuntu:wght@500;700&display=swap" rel="stylesheet">
<style>
  :root {
    --page-bg: #eef1f3;
    --white: #ffffff;
    --green: #7cc043;
    --blue: #1f6fa6;
    --blue-light: #3f8fc4;
    --teal: #3fb6c9;
    --nav-text: #5b6670;
  }
  * { box-sizing: border-box; margin: 0; padding: 0; }
  html, body {
    width: 1200px; height: 1200px; overflow: hidden;
    background: var(--page-bg);
    font-family: "Raleway", sans-serif;
  }
  .site {
    position: absolute; left: 40px; top: 250px;
    width: 1120px; height: 700px;
    background: var(--white);
    box-shadow: 0 10px 40px rgba(30, 50, 70, 0.12);
    overflow: hidden;
  }

  /* Header */
  .site-header { position: relative; height: 118px; background: var(--white); z-index: 2; }
  .brand {
    position: absolute; left: 20px; top: 0; width: 280px; height: 118px;
    display: flex; align-items: center; justify-content: center; gap: 8px;
  }
  .brand-dot { flex-shrink: 0; width: 12px; height: 12px; border-radius: 50%; background: var(--green); }
  .brand-name {
    font-family: "Ubuntu", sans-serif; font-weight: 700; font-size: 18px;
    color: var(--blue); white-space: nowrap;
  }
  .utility-bar {
    position: absolute; left: 310px; top: 20px; right: 0; height: 40px;
    background: var(--green);
    clip-path: polygon(30px 0, 100% 0, 100% 100%, 0 100%);
    display: flex; align-items: center; justify-content: flex-end;
    padding-right: 120px; gap: 16px;
    font-size: 12px; color: var(--white); white-space: nowrap;
  }
  .utility-bar .sep { opacity: 0.8; }
  .main-nav {
    position: absolute; left: 350px; top: 76px; right: 40px;
    display: flex; align-items: center; gap: 22px;
    font-size: 13px; color: var(--nav-text); white-space: nowrap;
  }
  .main-nav .is-active {
    color: var(--blue-light); border: 1px solid var(--blue-light);
    padding: 3px 6px;
  }
  .main-nav .cta {
    margin-left: auto; margin-right: 60px;
    color: var(--blue); border: 1px solid var(--blue);
    padding: 5px 10px; font-size: 13px; letter-spacing: 0.3px;
  }

  /* Hero slider */
  .hero {
    position: absolute; left: 0; top: 118px; width: 1120px; height: 520px;
  }
  .hero-photo {
    position: absolute; inset: 0;
    background:
      radial-gradient(ellipse 420px 360px at 300px 260px, #d9a88e 0%, rgba(217,168,142,0.55) 40%, rgba(217,168,142,0) 75%),
      linear-gradient(90deg, #c9d1cf 0%, #dfe3e2 45%, #eef0f0 70%, #f4f5f5 100%);
  }
  .hero-copy {
    position: absolute; left: 540px; top: 140px; width: 510px; text-align: center;
  }
  .hero-title {
    font-family: "Ubuntu", sans-serif; font-weight: 700;
    font-size: 42px; line-height: 1.2; color: var(--blue);
  }
  .hero-brand {
    margin-top: 34px; display: flex; align-items: center; justify-content: center; gap: 14px;
  }
  .hero-brand .brand-dot { width: 26px; height: 26px; }
  .hero-brand .brand-name { font-size: 32px; }
  .slider-arrow {
    position: absolute; width: 34px; height: 34px; border-radius: 50%;
    display: flex; align-items: center; justify-content: center;
  }
  .slider-arrow.prev { left: 90px; top: 230px; background: var(--teal); }
  .slider-arrow.next { right: 20px; top: 270px; background: var(--blue); }

  .hero-footer { position: absolute; left: 0; bottom: 0; width: 1120px; height: 62px; background: var(--white); }
</style>
</head>
<body>
  <div class="site">
    <header class="site-header">
      <div class="brand">
        <span class="brand-dot"></span>
        <span class="brand-name">Bright Oak Family Medicine</span>
      </div>
      <div class="utility-bar">
        <span>OakCare Membership</span><span class="sep">|</span>
        <span>FAQ</span><span class="sep">|</span>
        <span>Contact us</span>
      </div>
      <nav class="main-nav">
        <span class="is-active">Home</span>
        <span>Aboutus</span>
        <span>Services</span>
        <span>Resources</span>
        <span>Current Patients</span>
        <span>New Patients</span>
        <span class="cta">START HERE</span>
      </nav>
    </header>

    <section class="hero">
      <div class="hero-photo" role="img" aria-label="Photo of a smiling woman holding a coffee cup in a bright, softly lit room"></div>
      <div class="hero-copy">
        <h1 class="hero-title">WE Will Help<br>You To Make life Happy</h1>
        <div class="hero-brand">
          <span class="brand-dot"></span>
          <span class="brand-name">Bright Oak Family Medicine</span>
        </div>
      </div>
      <span class="slider-arrow prev">
        <svg width="12" height="12" viewBox="0 0 12 12"><path d="M8 1 L3 6 L8 11" fill="none" stroke="#fff" stroke-width="1.6"/></svg>
      </span>
      <span class="slider-arrow next">
        <svg width="12" height="12" viewBox="0 0 12 12"><path d="M4 1 L9 6 L4 11" fill="none" stroke="#fff" stroke-width="1.6"/></svg>
      </span>
    </section>
    <div class="hero-footer"></div>
  </div>
</body>
</html>
```